Quendra - Clear Spirit Cosmetics

Please design a logo and business cards for new food supplements, cosmetics and herbal fixatives. The products are produced ecologically and biologically in the South Tyrol and Trentino alps. The products are pure and noble. Quendra = pure vitality Colors Background: dark or black matt (soft touch) Logodesign: powerful, elegant, violet with glossy foil The logo and design should convey warmth, passion and the 6th sense, you should get the impression that you can smell the herbal odor , Logo and business cards for new food supplements, cosmetics and herbal fixatives. The products are produced ecologically and biologically in the South Tyrol and Trentino alps. The products are pure and noble. Quendra = pure vitality Colors Background: dark or black matt (softtouch) Logodesign: powerful elegant violet with glossy foil The logo and design is meant to convey warmth, passion and the 6th sense, you should get the impression that you can smell the herbal perfume.

Target Market(s)

Food, food supplements, vitality, health

Contact Information for Business Card

Please provide an elegant darf design that is puristic, but has a very good logo design
Elegantes dunkles design, puristisch

Logo Text

Quendra - clear Spirit

Colors
6b449b

Requirements
Must have
• SVG Files Alpha channel for foil embossing High-quality design
Nice to have
• Pure elegance
Should not have
• to colorful colors

```html
<!DOCTYPE html>
<html lang="en">
<head>
<meta charset="utf-8">
<title>Quendra - Clear Spirit Cosmetics · Business Cards</title>
<link rel="stylesheet" href="https://fonts.googleapis.com/css2?family=Exo+2:wght@400;600&display=swap">
<style>
  :root {
    --canvas-bg: #e9e7ec;
    --card-dark: #2f3035;
    --card-light: #ffffff;
    --violet: #6b449b;
    --violet-soft: #9a82c2;
    --violet-faint: #c9bde0;
    --ink: #1d1d22;
  }
  * { margin: 0; padding: 0; box-sizing: border-box; }
  html, body { width: 1200px; height: 892px; overflow: hidden; }
  body {
    background: var(--canvas-bg);
    font-family: "Exo 2", sans-serif;
    color: var(--ink);
    position: relative;
  }
  .card {
    position: absolute;
    top: 298px;
    width: 520px;
    height: 297px;
    border-radius: 3px;
    box-shadow: 0 10px 28px rgba(40, 30, 60, 0.18);
    overflow: hidden;
  }
  .card--back { left: 50px; background: var(--card-light); }
  .card--front { left: 630px; background: var(--card-dark); }

  /* back side */
  .swirl-art {
    position: absolute;
    left: 70px; top: 20px;
    width: 150px; height: 277px;
    background: linear-gradient(170deg, rgba(107,68,155,0.35), rgba(154,130,194,0.7));
    border-radius: 75px 75px 0 0;
  }
  .vine-art-left {
    position: absolute;
    left: 14px; top: 60px;
    width: 70px; height: 110px;
    background: linear-gradient(160deg, rgba(201,189,224,0.55), rgba(201,189,224,0.15));
    border-radius: 40px;
  }
  .vine-art-right {
    position: absolute;
    right: 0; top: 110px;
    width: 160px; height: 187px;
    background: linear-gradient(200deg, rgba(201,189,224,0.65), rgba(201,189,224,0.1));
    border-radius: 80px 0 0 0;
  }
  .identity { position: absolute; left: 250px; top: 40px; }
  .identity__name { font-size: 24px; font-weight: 600; line-height: 1.1; }
  .identity__role { font-size: 17px; font-weight: 400; margin-top: 4px; }
  .contact-list {
    position: absolute; left: 250px; top: 150px;
    list-style: none;
    font-size: 14.5px;
  }
  .contact-list li {
    display: flex; align-items: center; gap: 10px;
    height: 24px;
  }
  .contact-list svg { width: 15px; height: 15px; fill: var(--violet); flex: none; }

  /* front side */
  .vine-art-front-left {
    position: absolute; left: 0; top: 150px;
    width: 200px; height: 147px;
    background: linear-gradient(30deg, rgba(107,68,155,0.45), rgba(107,68,155,0.05));
    border-radius: 0 100px 0 0;
  }
  .vine-art-front-right {
    position: absolute; right: 0; top: 0;
    width: 210px; height: 90px;
    background: linear-gradient(210deg, rgba(107,68,155,0.45), rgba(107,68,155,0.05));
    border-radius: 0 0 0 90px;
  }
  .brand-mark {
    position: absolute; inset: 0;
    display: flex; align-items: center; justify-content: center;
    font-size: 76px; font-weight: 600;
    color: var(--violet);
    letter-spacing: 1px;
  }
</style>
</head>
<body>

  <section class="card card--back" aria-label="Business card, contact side">
    <div class="vine-art-left" role="img" aria-label="Faint violet floral vine ornament"></div>
    <div class="swirl-art" role="img" aria-label="Large violet flowing swirl ornament"></div>
    <div class="vine-art-right" role="img" aria-label="Light violet leafy vine ornament"></div>

    <div class="identity">
      <p class="identity__name">Your Name</p>
      <p class="identity__role">Operations Manager</p>
    </div>

    <ul class="contact-list">
      <li>
        <svg viewBox="0 0 24 24"><path d="M6.6 10.8a15.1 15.1 0 0 0 6.6 6.6l2.2-2.2c.3-.3.7-.4 1-.2 1.1.4 2.3.6 3.6.6.6 0 1 .4 1 1V20c0 .6-.4 1-1 1A17 17 0 0 1 3 4c0-.6.4-1 1-1h3.5c.6 0 1 .4 1 1 0 1.3.2 2.5.6 3.6.1.3 0 .7-.2 1z"/></svg>
        <span>+1 (0)123456789</span>
      </li>
      <li>
        <svg viewBox="0 0 24 24"><path d="M2 5h20v14H2zm2 2v.5l8 5 8-5V7l-8 5z"/></svg>
        <span>email@mailhost.com</span>
      </li>
      <li>
        <svg viewBox="0 0 24 24"><path d="M12 2a10 10 0 1 0 0 20 10 10 0 0 0 0-20zm6.9 9h-3a15 15 0 0 0-1.3-5.6A8 8 0 0 1 18.9 11zM12 4c.9 1.3 1.8 3.8 1.9 7h-3.8c.1-3.2 1-5.7 1.9-7zM9.4 5.4A15 15 0 0 0 8.1 11h-3a8 8 0 0 1 4.3-5.6zM5.1 13h3a15 15 0 0 0 1.3 5.6A8 8 0 0 1 5.1 13zM12 20c-.9-1.3-1.8-3.8-1.9-7h3.8c-.1 3.2-1 5.7-1.9 7zm2.6-1.4a15 15 0 0 0 1.3-5.6h3a8 8 0 0 1-4.3 5.6z"/></svg>
        <span>www.website.com</span>
      </li>
      <li>
        <svg viewBox="0 0 24 24"><path d="M12 2a7 7 0 0 0-7 7c0 5 7 13 7 13s7-8 7-13a7 7 0 0 0-7-7zm0 9.5a2.5 2.5 0 1 1 0-5 2.5 2.5 0 0 1 0 5z"/></svg>
        <span>Your Adress</span>
      </li>
    </ul>
  </section>

  <section class="card card--front" aria-label="Business card, brand side">
    <div class="vine-art-front-left" role="img" aria-label="Dark violet floral vine ornament"></div>
    <div class="vine-art-front-right" role="img" aria-label="Dark violet leafy vine ornament"></div>
    <p class="brand-mark">Quendra</p>
  </section>

</body>
</html>
```